Harbourline Metro Business Racquet Circuit (est.1952)

The Metro Business Racquet Circuit began in 1952 and has been played every year since. It is the longest running continuous sporting competition in the Sydney CBD. It is a team squash competition from May to Oct yearly played between companies, sporting groups or just a groups of friends.
We are looking for a flyer that we can reuse every year (so the content within the flyer can't be tied to a specific time). Other specific we are looking for are
1. Squash imagery (can either be real or graphic design) depicting action / athleticism / friendly rivalry
2. Needs the following content
a ) "A Sydney CBD based competition for friendly rivalry between companies, sporting clubs or between friends"
b) "All matches in and around the CBD from 5.30pm to 8pm"
c) "We cater for all playing abilities"
d) "Ladies beginner comp includes complimentary coaching"
e) "Visit our website www.plvqn.org.au for more info or contact Walter on frontw@qmx.com.au"

Flyer needs to include the logos attached in file upload section

```html
<!DOCTYPE html>
<html lang="en">
<head>
<meta charset="utf-8">
<title>Harbourline Metro Business Racquet Circuit</title>
<link rel="stylesheet" href="https://fonts.googleapis.com/css2?family=Anton&family=Oswald:wght@400;500&family=Poppins:wght@400;500;600;700&display=swap">
<style>
  :root {
    --navy: #1d2f6b;
    --navy-deep: #121f55;
    --yellow: #f5c21b;
    --yellow-deep: #e9a90e;
    --red: #d0333d;
    --line-red: #c9474c;
    --paper: #f2f2f3;
    --paper-shade: #d6d7da;
    --tick: #3bb54a;
    --white: #ffffff;
  }
  * { box-sizing: border-box; margin: 0; padding: 0; }
  html, body { width: 740px; height: 1200px; overflow: hidden; background: var(--white); }
  .flyer {
    position: relative; width: 740px; height: 1200px; overflow: hidden;
    background: radial-gradient(ellipse at 50% 45%, var(--paper) 0%, #e4e5e7 60%, var(--paper-shade) 100%);
    font-family: "Poppins", sans-serif; color: var(--navy);
  }
  .abs { position: absolute; }
  .corner-shapes, .court { position: absolute; left: 0; }
  .corner-shapes { top: 0; width: 740px; height: 620px; }

  .club-mark { top: 38px; left: 0; width: 740px; text-align: center; }
  .club-mark .dot { display: block; width: 62px; height: 62px; border-radius: 50%; background: var(--navy); margin: 0 auto 10px; }
  .club-mark .name { font-weight: 700; font-size: 20px; letter-spacing: 1px; color: var(--navy); }

  .org-name { top: 184px; width: 740px; text-align: center; font-weight: 700; font-size: 38px; color: var(--red); letter-spacing: 0.5px; }
  .title-art { top: 236px; left: 90px; width: 560px; height: 200px; }
  .ribbon-text { top: 248px; width: 740px; text-align: center; font-weight: 600; font-size: 25px; color: var(--navy); letter-spacing: 0.5px; }
  .headline { top: 318px; width: 740px; text-align: center; font-family: "Anton", sans-serif; font-size: 70px; line-height: 1; color: var(--white); letter-spacing: 0.5px; }
  .est { top: 442px; width: 740px; text-align: center; font-size: 22px; font-weight: 500; letter-spacing: 3px; color: #333; }

  .court-line { left: 0; width: 740px; height: 4px; background: var(--line-red); }
  .court-line.upper { top: 690px; }
  .court-line.lower { top: 920px; }

  .player-photo { top: 478px; left: 268px; width: 236px; height: 520px; border-radius: 40% 40% 8px 8px;
    background: linear-gradient(170deg, rgba(29,47,107,0.55) 0%, rgba(40,70,150,0.5) 45%, rgba(176,126,96,0.45) 75%, rgba(40,110,190,0.4) 100%); }

  .when { top: 510px; left: 58px; width: 200px; font-size: 18px; font-weight: 500; line-height: 1.25; }
  .when-rule { top: 578px; left: 58px; width: 130px; height: 2px; background: var(--yellow); }
  .ball { top: 571px; left: 196px; width: 15px; height: 15px; border-radius: 50%; background: var(--navy); }
  .clock { top: 600px; left: 56px; width: 46px; height: 46px; }
  .time { top: 596px; left: 112px; font-family: "Oswald", sans-serif; font-weight: 500; font-size: 34px; line-height: 1; color: var(--navy); }
  .time small { font-size: 22px; }
  .season { top: 638px; left: 112px; font-size: 13px; font-weight: 500; }

  .compete { top: 712px; left: 58px; width: 200px; font-size: 18px; font-weight: 600; line-height: 1.25; }
  .reasons { top: 770px; left: 58px; width: 200px; list-style: none; font-size: 13.5px; line-height: 1.2; }
  .reasons li { position: relative; padding-left: 22px; margin-bottom: 10px; }
  .reasons li svg { position: absolute; left: 0; top: 2px; width: 12px; height: 12px; }

  .abilities { top: 512px; left: 520px; width: 200px; font-size: 26px; line-height: 1.2; }
  .abilities strong { display: block; font-weight: 700; }
  .ladies { top: 730px; left: 520px; width: 190px; font-size: 18px; font-weight: 500; line-height: 1.25; }

  .court { top: 940px; width: 740px; height: 150px; }
  .info { top: 1020px; left: 58px; padding-left: 10px; border-left: 2px solid var(--navy); font-size: 14px; line-height: 1.2; }
  .url { top: 1028px; left: 188px; padding: 6px 14px; border-radius: 16px; background: var(--navy); color: var(--white); font-size: 13.5px; font-weight: 500; letter-spacing: 1px; }
  .contact { top: 1018px; right: 40px; text-align: right; color: var(--white); font-size: 13.5px; font-weight: 500; }
  .contact .email { display: block; color: var(--yellow); font-size: 16px; letter-spacing: 0.5px; }

  .sponsors { top: 1090px; left: 0; width: 740px; height: 110px; background: var(--white); }
  .sponsor-label-bg { top: 1090px; left: 0; width: 340px; height: 110px; }
  .sponsor-label { top: 1116px; left: 46px; font-family: "Oswald", sans-serif; font-size: 40px; line-height: 1.2; color: var(--yellow); letter-spacing: 0.5px; }
  .sponsor { top: 1118px; display: flex; flex-direction: column; align-items: center; gap: 6px; font-size: 12px; font-weight: 600; color: var(--navy); }
  .sponsor .mark { width: 34px; height: 34px; border-radius: 50%; }
  .sponsor.one { left: 362px; }
  .sponsor.one .mark { background: var(--red); }
  .sponsor.two { left: 478px; top: 1114px; }
  .sponsor.two .badge { width: 52px; height: 52px; border-radius: 50%; background: var(--navy); border: 3px solid var(--yellow-deep); }
  .sponsor.three { left: 575px; flex-direction: row; gap: 8px; font-size: 13px; line-height: 1.1; }
  .sponsor.three .mark { background: #4cb6d6; }
  .divider { top: 1118px; width: 2px; height: 50px; background: var(--navy); }
  .divider.a { left: 448px; }
  .divider.b { left: 555px; }
</style>
</head>
<body>
<main class="flyer">
  <svg class="corner-shapes" viewBox="0 0 740 620" aria-hidden="true">
    <path d="M0 0 H150 L120 30 L95 70 L60 95 L45 140 L20 170 L0 200 Z" fill="var(--navy)"/>
    <path d="M610 0 H740 V620 L712 560 L725 500 L700 450 L715 380 L690 330 L705 260 L680 210 L700 150 L660 110 L670 60 L630 40 Z" fill="var(--yellow)"/>
  </svg>

  <div class="abs club-mark">
    <span class="dot"></span>
    <span class="name">METRO COURT SQUASH</span>
  </div>

  <h2 class="abs org-name">HARBOURLINE</h2>
  <svg class="abs title-art" viewBox="0 0 560 200" aria-hidden="true">
    <path d="M55 58 L85 46 L475 46 L505 58 L545 120 L535 185 L25 195 L15 120 Z" fill="var(--navy)"/>
    <path d="M80 10 H480 L470 28 L488 48 H72 L90 28 Z" fill="var(--yellow)"/>
    <path d="M72 48 L90 58 L90 48 Z M488 48 L470 58 L470 48 Z" fill="var(--yellow-deep)"/>
  </svg>
  <p class="abs ribbon-text">METRO BUSINESS</p>
  <h1 class="abs headline">RACQUET CIRCUIT</h1>
  <p class="abs est">(EST.1952)</p>

  <div class="abs court-line upper"></div>
  <div class="abs court-line lower"></div>

  <svg class="court" viewBox="0 0 740 150" preserveAspectRatio="none" aria-hidden="true">
    <path d="M0 0 C200 -5 600 10 740 40 V150 H0 Z" fill="var(--navy)"/>
    <path d="M0 22 C230 15 430 30 470 70 C500 110 470 140 440 150 H0 Z" fill="var(--white)"/>
    <path d="M0 34 C220 28 410 40 448 75 C475 110 455 140 420 150 H0 Z" fill="var(--yellow)"/>
  </svg>

  <div class="abs player-photo" role="img" aria-label="Photo of a squash player lunging forward to play a backhand shot"></div>

  <p class="abs when">All matches in and around the CBD from</p>
  <div class="abs when-rule"></div>
  <div class="abs ball"></div>
  <svg class="abs clock" viewBox="0 0 46 46" aria-hidden="true">
    <circle cx="23" cy="23" r="20" fill="var(--yellow)" stroke="var(--navy)" stroke-width="3"/>
    <path d="M23 11 V23 L31 28" fill="none" stroke="var(--navy)" stroke-width="3" stroke-linecap="round"/>
  </svg>
  <p class="abs time">5.30PM <small>TO</small> 8PM</p>
  <p class="abs season">May to Oct yearly</p>

  <p class="abs compete">A Sydney CBD based competition for :</p>
  <ul class="abs reasons">
    <li><svg viewBox="0 0 12 12"><circle cx="6" cy="6" r="6" fill="var(--tick)"/><path d="M3 6 L5.2 8 L9 4" fill="none" stroke="#fff" stroke-width="1.6"/></svg>Friendly rivalry between companies</li>
    <li><svg viewBox="0 0 12 12"><circle cx="6" cy="6" r="6" fill="var(--tick)"/><path d="M3 6 L5.2 8 L9 4" fill="none" stroke="#fff" stroke-width="1.6"/></svg>Sporting clubs or<br>between friends</li>
  </ul>

  <p class="abs abilities"><strong>We cater for</strong> all playing abilities</p>
  <p class="abs ladies">Ladies beginner comp includes complimentary coaching</p>

  <p class="abs info">For more info<br>Visit our website</p>
  <p class="abs url">WWW.PLVQN.ORG.AU</p>
  <p class="abs contact">Contact Walter on <span class="email">frontw@qmx.com.au</span></p>

  <div class="abs sponsors"></div>
  <svg class="abs sponsor-label-bg" viewBox="0 0 340 110" aria-hidden="true">
    <path d="M0 0 H340 L290 110 H0 Z" fill="var(--yellow)"/>
    <path d="M0 0 H326 L276 110 H0 Z" fill="var(--navy-deep)"/>
  </svg>
  <p class="abs sponsor-label">SPONSORED BY</p>
  <div class="abs sponsor one"><span class="mark"></span>PLVQN</div>
  <div class="abs divider a"></div>
  <div class="abs sponsor two"><span class="badge"></span></div>
  <div class="abs divider b"></div>
  <div class="abs sponsor three"><span class="mark"></span><span>BAYSIDE COURT<br>ACADEMY</span></div>
</main>
</body>
</html>
```